4D Hush Little Nest Luxury Ultrasound Billboard

Design a HIGH-END, MODERN billboard for my private prenatal ultrasound studio, 4D Hush Little Nest, located in Pace, Florida.
This billboard will be viewed by drivers traveling at highway speeds, so it must be extremely clean, simple, and readable within 6 seconds.
About My Business
4D Hush Little Nest is a private prenatal ultrasound studio specializing in:
Highest technology 4D/HD Ultrasounds
Early Gender Determination
Pregnancy Confirmation
I have been serving families for nearly 10 years and is known for creating a memorable experience, not just an ultrasound appointment.
Design Style
I DO NOT want:
Flowers
Leaves
Swirls
Glitter
Hearts everywhere
Busy backgrounds
Generic maternity stock graphics
I DO want:
Modern
Luxury
Upscale
Clean
Professional
Eye-catching
Premium medical spa feel
Colors
Use colors from my logo:
LOGO Green ( or a deep green)
Black
White
Soft Gold accents
Images:
Incorporate my professional headshot in a clean, modern way, logo, and the ultrasound images
Text
Keep wording minimal.
Primary Headline ( OPEN TO IDEAS) :
EXAMPLES ( WOULD RATHER SOMETHING MORE CATCHY)
" ADVANCED IMAGING. UNFORGETTABLE MOMENTS"
"MEET YOUR BABY BEFORE BIRTH"
Under headline:
4D Ultrasound • Early Gender • Pregnancy Confirmation
Business Name:
4D Hush Little Nest
Private Prenatal Ultrasound Studio
Phone Number:
850-471-3905
Important
This billboard must be readable in 5–6 seconds from a moving vehicle.
Less text is better.
The phone number and business name must be visible from a distance.
The design should feel like a premium brand that immediately tells expecting parents:
“This is where I go to see my baby.”
Files Provided
Official logo
Headshot
Ultrasound images
Don’t make this look like a medical office billboard.
Make it look like a luxury baby experience billboard. That’s what separates 4D Hush Little Nest from hospitals, OB offices, and all the new studios popping up around you. The emotional connection is what gets moms to book. ❤️
Billboard Size - 10.6” x 36”

```html
<!DOCTYPE html>
<html lang="en">
<head>
<meta charset="utf-8">
<title>4D Hush Little Nest Billboard</title>
<link rel="stylesheet" href="https://fonts.googleapis.com/css2?family=Cormorant+Garamond:ital,wght@0,500;0,600;1,600&family=Montserrat:wght@500;700&display=swap">
<style>
  :root {
    --ink: #0d0c08;
    --paper: #ffffff;
    --gold: #c9aa5a;
    --green: #4a5a4d;
    --photo-light: #e6e6e8;
    --photo-mid: #8d918c;
  }
  * { margin: 0; padding: 0; box-sizing: border-box; }
  html, body { width: 1200px; height: 353px; overflow: hidden; background: var(--paper); }
  .billboard {
    position: relative;
    width: 1200px;
    height: 353px;
    background: var(--ink);
    border-top: 1px solid #2a2a22;
    overflow: hidden;
  }
  .edge-strip {
    position: absolute; left: 0; top: 0; width: 17px; height: 100%;
    background: var(--paper);
  }
  .headshot {
    position: absolute; left: 17px; top: 0; width: 241px; height: 100%;
    background:
      radial-gradient(ellipse 55% 45% at 45% 70%, rgba(58,78,62,0.75), transparent 70%),
      linear-gradient(90deg, var(--photo-light) 0%, #c9cacb 45%, var(--photo-mid) 80%, #3d3e3a 100%);
  }
  .eyebrow {
    position: absolute; left: 287px; top: 103px;
    font-family: "Montserrat", sans-serif; font-weight: 500;
    font-size: 10px; letter-spacing: 5.2px;
    color: var(--gold);
  }
  .headline {
    position: absolute; left: 288px; top: 124px;
    font-family: "Cormorant Garamond", serif; font-weight: 600;
    font-size: 50px; line-height: 56px;
    color: var(--paper);
  }
  .headline em {
    display: block; font-style: italic; color: var(--gold);
  }
  .services {
    position: absolute; left: 285px; top: 256px;
    font-family: "Montserrat", sans-serif; font-weight: 500;
    font-size: 9.6px; letter-spacing: 4.1px;
    color: var(--paper);
    white-space: nowrap;
  }
  .services .dot { color: var(--paper); margin: 0 4px; }
  .brand-tile {
    position: absolute; left: 1007px; top: 60px; width: 133px; height: 172px;
    background: var(--paper);
    display: flex; align-items: center; justify-content: center;
    text-align: center;
    font-family: "Cormorant Garamond", serif; font-weight: 600;
    font-size: 22px; line-height: 25px;
    color: var(--green);
    padding: 0 10px;
  }
  .cta {
    position: absolute; left: 974px; top: 251px; width: 200px;
    text-align: center; color: var(--paper);
    font-family: "Montserrat", sans-serif;
  }
  .cta-label {
    font-weight: 500; font-size: 9.6px; letter-spacing: 4.6px;
    padding-left: 4px;
  }
  .cta-phone {
    font-weight: 700; font-size: 25px; letter-spacing: 0.2px;
    margin-top: 4px;
  }
</style>
</head>
<body>
  <main class="billboard">
    <div class="edge-strip"></div>
    <div class="headshot" role="img" aria-label="Portrait of the sonographer seated in her ultrasound studio holding a probe"></div>

    <p class="eyebrow">PRIVATE PRENATAL ULTRASOUND STUDIO</p>
    <h1 class="headline">See Your Baby<em>Before Birth</em></h1>
    <p class="services">4D ULTRASOUND<span class="dot">▪</span> EARLY GENDER<span class="dot">▪</span> PREGNANCT CONFIRMATION</p>

    <div class="brand-tile">4D Hush Little Nest</div>

    <div class="cta">
      <p class="cta-label">BOOK TODAY</p>
      <p class="cta-phone">850-471-3905</p>
    </div>
  </main>
</body>
</html>
```